Psychology Practice in Sydney Website Redesign

Corlew Psychology is a Psychology Practice with locations in Westmead, Chatswood and the CBD. They have specialties in treating children, and in treating eating disorders. They also treat anxiety and depression. They have ~10-20 clinical psychologists working for them.

The client wants the site to be modern and professional, he said:
”Mainly gonna be the credibility, people already know of us, but some could find us on google search, site needs to be a bit sexy.”

The client prefers websites with a heavy use of negative space and a largely minimal, modern design. (e.g. https://harbourlanemind-example.com.au/, https://www.fenmora-example.net.au/, https://tovalin-example.com.au/). He wants the site to be approachable without being unprofessional, and to be modern without being clinical. This is their current site: https://www.corlewpsychology-example.com.au/

The client wants the site to be a one pager design (like the sites given above). Please include a section named “Our Specialisations”, and the next titled “What we treat”, then one titled “Our Team” Feel free to take inspiration from the included links for the layout of these parts of the site.

Please mock up a booking panel similar to the that appears when you click "book now" on https://www.quillbrookcare-example.com.au/# .

The client would prefer you use the current logo and colour green (in logo) for theming.

Current site: https://www.corlewpsychology-example.com.au/

The winning designers will be required to:
- Provide a secondary standard page template
- Provide a design for a flyout enquiry/booking form
- Supply all images used in the designs free of charge

```html
<!DOCTYPE html>
<html lang="en">
<head>
<meta charset="utf-8">
<title>Corlew &amp; Associates — Clinical Psychologists</title>
<link rel="stylesheet" href="https://fonts.googleapis.com/css2?family=Jost:wght@400;500;600&family=Lato:wght@400;700&display=swap">
<style>
:root{
  --green:#6fbf88;
  --green-soft:#eefbf2;
  --ink:#1f1f1f;
  --text:#333;
  --muted:#7a7a7a;
  --dark:#2f2b2b;
  --white:#fff;
  --line:#dcdcdc;
}
*{box-sizing:border-box;margin:0;padding:0}
html,body{width:1200px;height:4118px;overflow:hidden;background:var(--white)}
body{font-family:"Lato",sans-serif;color:var(--text)}
.page{position:relative;width:1200px;height:4118px}
.abs{position:absolute}
.heading{font-family:"Jost",sans-serif;font-weight:500;text-transform:uppercase}
.hl{background:var(--green);color:var(--white);padding:0 10px}
.btn{position:absolute;display:flex;align-items:center;justify-content:center;background:var(--green);color:var(--white);font-family:"Jost",sans-serif;font-weight:600;font-size:17px;letter-spacing:.5px;text-decoration:none;text-transform:uppercase}
.link{font-family:"Jost",sans-serif;font-weight:600;text-decoration:underline;text-transform:uppercase;color:inherit}

/* nav */
.nav{left:0;top:0;width:1200px;height:85px;background:var(--green)}
.brand{left:51px;top:22px;color:var(--white);font-family:"Jost",sans-serif;font-weight:600;font-size:26px;letter-spacing:-.3px}
.nav-menu{left:408px;top:33px;display:flex;gap:46px;font-family:"Jost",sans-serif;font-size:15px;color:var(--white);list-style:none;text-transform:uppercase}
.nav-menu .active{background:var(--white);color:var(--green);padding:3px 8px;margin:-3px -8px;font-weight:600}
.nav-cta{left:1008px;top:19px;width:130px;height:47px;background:var(--white);color:var(--green);font-size:15px}

/* hero */
.hero-bg{left:0;top:85px;width:420px;height:553px;background:linear-gradient(120deg,var(--green-soft),#fff 70%)}
.hero-photo{left:420px;top:85px;width:780px;height:553px;background:linear-gradient(135deg,#8a7d73,#5d5f66 45%,#a59c92)}
.hero-title{left:110px;top:207px;font-size:34px;line-height:51px;color:var(--green);z-index:2}
.hero-title .hl{padding:0 6px}
.hero-copy{left:110px;top:372px;width:260px;font-size:15px;line-height:27px;color:var(--ink)}
.hero-btn{left:110px;top:449px;width:160px;height:51px}

/* section titles */
.sec-title{left:0;width:1200px;text-align:center;font-size:44px;color:var(--green)}
.rule{left:110px;width:978px;height:1px;background:var(--line)}

/* treat cards */
.treat{top:799px;width:301px;height:316px;background:var(--dark);color:var(--white);text-align:center;padding-top:34px}
.treat.featured{background:var(--green);padding-top:43px}
.treat svg{width:40px;height:46px}
.treat h3{font-family:"Jost",sans-serif;font-weight:500;font-size:25px;color:var(--green);margin:14px 0 10px}
.treat.featured h3{color:var(--white)}
.treat p{font-size:15px;line-height:27px;padding:0 34px;margin-bottom:20px}
.treat .link{font-size:14px}

/* specialisations */
.spec-photo{width:489px;height:477px}
.photo-kids{left:110px;top:1417px;background:linear-gradient(135deg,#e7e1d8,#c79b78 55%,#f2ece4)}
.photo-food{left:599px;top:1895px;background:linear-gradient(160deg,#9a9a9a,#b9b6b0 50%,#d8d3c8 70%,#8fb55a)}
.accent{background:var(--green)}
.spec-text{width:402px}
.spec-text h3{font-family:"Jost",sans-serif;font-weight:500;font-size:25px;color:var(--ink);margin-bottom:18px;text-transform:uppercase}
.spec-text p{font-size:15px;line-height:27.5px;color:var(--ink);margin-bottom:26px}

/* team */
.member{top:2659px;width:221px;height:385px;background:var(--white);box-shadow:0 2px 10px rgba(0,0,0,.12);text-align:center;padding:31px 14px 0}
.avatar{width:86px;height:86px;border-radius:50%;margin:0 auto 20px;background:linear-gradient(160deg,#c9a58a,#7f5a45)}
.member h4{font-family:"Jost",sans-serif;font-weight:600;font-size:15px;color:var(--ink);text-transform:uppercase}
.creds{font-size:12px;color:var(--muted);margin:9px 0 14px}
.member p{font-size:12.5px;line-height:24px;color:var(--muted);margin-bottom:8px;height:144px;overflow:hidden}
.member .link{font-size:12px;color:var(--ink)}

/* about */
.about{left:0;top:3252px;width:1200px;height:444px;background:linear-gradient(90deg,#2a2c28,#3a3a35 50%,#2d2f2b)}
.about-title{top:3322px;font-size:44px}
.about-title .lead{color:var(--green)}
.about-copy{left:180px;width:840px;text-align:center;font-size:15px;line-height:29px;color:var(--white)}

/* footer */
.foot-brand{left:110px;top:3786px;color:var(--green);font-family:"Jost",sans-serif;font-weight:600;font-size:24px}
.foot-col h5{font-family:"Jost",sans-serif;font-weight:500;font-size:19px;color:var(--ink);margin-bottom:12px;text-transform:uppercase}
.foot-col ul{list-style:none;padding-left:5px}
.foot-col li{font-size:15px;line-height:29px;color:var(--ink)}
.copy{left:0;top:4056px;width:1200px;text-align:center;font-family:"Jost",sans-serif;font-size:15px;color:var(--ink)}
</style>
</head>
<body>
<div class="page">

  <header class="abs nav">
    <div class="abs brand">CORLEW &amp; ASSOCIATES</div>
    <ul class="abs nav-menu">
      <li><span class="active">Home</span></li>
      <li>Our Specialisation</li>
      <li>What we treat</li>
      <li>Our Team</li>
    </ul>
    <a class="btn nav-cta">Contact us</a>
  </header>

  <section>
    <div class="abs hero-bg"></div>
    <div class="abs hero-photo" role="img" aria-label="Psychologist in session with a client seated on a sofa"></div>
    <h1 class="abs heading hero-title">We specialise in <span class="hl">many areas.</span><br>Find the right <span class="hl">psychologist</span><br>for you</h1>
    <p class="abs hero-copy">Everyone is susceptible to emotional issues at some stage in their life.</p>
    <a class="btn hero-btn">Book now</a>
  </section>

  <section>
    <h2 class="abs heading sec-title" style="top:706px">What we <span class="hl">treat</span></h2>

    <article class="abs treat" style="left:110px">
      <svg viewBox="0 0 40 46" fill="#6fbf88"><circle cx="20" cy="14" r="5"/><path d="M10 44l4-18h12l4 18h-5l-3-10-2 10h-2l-2-10-3 10z"/><path d="M8 2l4 6M32 2l-4 6M20 0v5" stroke="#6fbf88" stroke-width="2.5"/></svg>
      <h3>ANXIETY</h3>
      <p>People have come to recognise the benefits of professional treatment for a better future.</p>
      <a class="link">Read more</a>
    </article>

    <article class="abs treat featured" style="left:449px">
      <svg viewBox="0 0 40 46" fill="#fff"><path d="M2 20h36a18 18 0 0 1-36 0z"/><circle cx="14" cy="15" r="4"/><circle cx="22" cy="13" r="5"/><path d="M28 16l8-12" stroke="#fff" stroke-width="2.5"/></svg>
      <h3>EATING DISORDERS</h3>
      <p>People have come to recognise the benefits of professional treatment for a better future.</p>
      <a class="link">Read more</a>
    </article>

    <article class="abs treat" style="left:788px">
      <svg viewBox="0 0 40 46" fill="#6fbf88"><path d="M20 2a16 16 0 0 0-16 16c0 6 3 9 5 12v14h16v-6h6a3 3 0 0 0 3-3v-6h3l-4-8A16 16 0 0 0 20 2z"/><circle cx="19" cy="18" r="7" fill="none" stroke="#2f2b2b" stroke-width="2"/><path d="M15 22a5 4 0 0 1 8 0" fill="none" stroke="#2f2b2b" stroke-width="2"/></svg>
      <h3>DEPRESSION</h3>
      <p>People have come to recognise the benefits of professional treatment for a better future.</p>
      <a class="link">Read more</a>
    </article>
  </section>

  <div class="abs rule" style="top:1210px"></div>

  <section>
    <h2 class="abs heading sec-title" style="top:1290px">Our <span class="hl">Specialisations</span></h2>

    <div class="abs accent" style="left:0;top:1793px;width:110px;height:102px"></div>
    <div class="abs spec-photo photo-kids" role="img" aria-label="Mother and daughter baking cupcakes together in a kitchen"></div>
    <div class="abs spec-text" style="left:687px;top:1497px">
      <h3>Treating children</h3>
      <p>Our range of fully qualified clinical psychologists means that we can find the right person for you.Psychological therapy can readily be adapted to the online medium.</p>
      <p>Everyone is susceptible to emotional issues at some stage in their life. People have come to recognise the benefits of professional treatment for a better future.</p>
    </div>
    <a class="btn" style="left:687px;top:1759px;width:158px;height:51px">Read more</a>

    <div class="abs spec-text" style="left:110px;top:1975px">
      <h3>Treating eating disorders</h3>
      <p>Our range of fully qualified clinical psychologists means that we can find the right person for you.Psychological therapy can readily be adapted to the online medium.</p>
      <p>Everyone is susceptible to emotional issues at some stage in their life. People have come to recognise the benefits of professional treatment for a better future.</p>
    </div>
    <a class="btn" style="left:110px;top:2237px;width:158px;height:51px">Read more</a>
    <div class="abs spec-photo photo-food" role="img" aria-label="Young woman reluctantly looking at a plate of vegetables"></div>
    <div class="abs accent" style="left:1088px;top:2271px;width:112px;height:100px"></div>
  </section>

  <div class="abs rule" style="top:2469px"></div>

  <section>
    <h2 class="abs heading sec-title" style="top:2546px">Our <span class="hl">Team</span></h2>

    <article class="abs member" style="left:110px">
      <div class="avatar" role="img" aria-label="Portrait of Maren Holloway"></div>
      <h4>Maren Holloway</h4>
      <div class="creds">B.Psych (Hons), M.Psych (Clinical)</div>
      <p>Maren is a Clinical Psychology Registrar who completed her Master of Clinical Psychology and Bachelor of Psychology (Honours) at Harbourside University.</p>
      <a class="link">Read more</a>
    </article>
    <article class="abs member" style="left:363px">
      <div class="avatar" role="img" aria-label="Portrait of Elise Varden"></div>
      <h4>Elise Varden</h4>
      <div class="creds">B.Sc. (Psych)(Hons); MClinPsych</div>
      <p>Elise is a Clinical Psychology Registrar who completed her Master of Clinical Psychology at Northfield University after gaining a Bachelor of Science with Psychology Honours at the</p>
      <a class="link">Read more</a>
    </article>
    <article class="abs member" style="left:615px">
      <div class="avatar" role="img" aria-label="Portrait of Joanne Pellew"></div>
      <h4>Joanne Pellew</h4>
      <div class="creds">B.Psych (Hons), M.Psych (Clinical)</div>
      <p>Joanne is a Clinical Psychology Registrar who completed her Master of Clinical Psychology and Bachelor of Psychology (Honours) at Harbourside University.</p>
      <a class="link">Read more</a>
    </article>
    <article class="abs member" style="left:866px">
      <div class="avatar" role="img" aria-label="Portrait of Callum Restrick"></div>
      <h4>Callum Restrick</h4>
      <div class="creds">B.Sc. (Psych)(Hons); MClinPsych</div>
      <p>Callum is a Clinical Psychology Registrar who completed his Master of Clinical Psychology at Northfield University after gaining a Bachelor of Science with Psychology Honours at the</p>
      <a class="link">Read more</a>
    </article>

    <a class="btn" style="left:524px;top:3110px;width:150px;height:49px">View more</a>
  </section>

  <section>
    <div class="abs about" role="img" aria-label="Dimmed photo of a psychologist talking with a client"></div>
    <h2 class="abs heading sec-title about-title"><span class="lead">About </span><span class="hl">Corlew &amp; Associates</span></h2>
    <p class="abs about-copy" style="top:3403px">Everyone is susceptible to emotional issues at some stage in their life. People have come to recognise the benefits of professional treatment for a better future. 1000’s of people have received help from us in the last 20 years.</p>
    <p class="abs about-copy" style="top:3492px">A change in your life can begin right now.&nbsp; We can help. Our range of fully qualified clinical psychologists means that we can find the right person for you.</p>
    <a class="btn" style="left:524px;top:3587px;width:151px;height:50px">Read more</a>
  </section>

  <footer>
    <div class="abs foot-brand">CORLEW &amp; ASSOCIATES</div>
    <div class="abs foot-col" style="left:455px;top:3778px">
      <h5>Quick links</h5>
      <ul><li>Home</li><li>About</li><li>Our Specialisations</li><li>What we treat</li><li>Team</li><li>Contact us</li></ul>
    </div>
    <div class="abs foot-col" style="left:657px;top:3778px">
      <h5>Help links</h5>
      <ul><li>FAQ</li><li>Term of use</li><li>Privacy Policy</li><li>Support Links</li><li>Terms &amp; Conditions</li></ul>
    </div>
    <div class="abs foot-col" style="left:829px;top:3778px">
      <h5>Contact us</h5>
      <ul><li>Corlew &amp; Associates</li><li>PO Box 512, Parkvale NSW 2199</li><li>Phone: (02) 9000 4821</li><li>Email: info@corlew-example.com.au</li></ul>
    </div>
    <div class="abs rule" style="top:4019px"></div>
    <p class="abs copy">Copyrights@2024.Corlew &amp; Associates.All Rights Reserved</p>
  </footer>

</div>
</body>
</html>
```